Life/Executive Coach and Trainer needs a business card

I would need a clean, very modern and distinctive business card incl. logo (I have a slight preference for a hexagonal shape or things like the tree - see files uploaded), although I am open to new things. My business is called "Brightway" (=first line) and then "Beratung & Training" (=second line). Please see the graphics file attached as and idea, where "MARLOWE" would be "BRIGHTWAY" and "Company Sitebuilder Layout" would be "Beratung & Training". However, this is just an idea, I am very open for new designs and ideas! The logo should reflect the name "Brightway" (meaning unity; one not without the other; symbiosis; balance; equilibrium). I am offering life/executive coaching as well as attention and stress management trainings for individuals or business teams by using innovative, combined methods of yoga, meditation and others. My services are offered locally in my office, at the client's office but also online via Zoom/Skype.

Target Market(s)

Private persons or corporate executives as well as business teams, experts and managers

Industry/Entity Type

Consultant

Contact Information for Business Card

My name should appear in one line (please see uploaded docx-file "Name") as: Mag. Lukas Brandauer, MSc (the "Mag." and the "MSc" should be in smaller letters as they are just academic titles and not part of my name).

Address: Praxis Top 3, Kellergasse 48/2, 1020 Wien
Phone: +43 660 8273916
Email: info@brightway-coaching.eu
Website: www.brightway-coaching.eu

The business card must also show:
- Coaching & Supervision
- Aufmerksamkeitstraining
- Stressmanagement

Font styles to use
Sans Serif

Requirements
Must have
• Cutting-edge, clean and modern design

```html
<!DOCTYPE html>
<html lang="de">
<head>
<meta charset="utf-8">
<title>Brightway – Beratung &amp; Training – Visitenkarte</title>
<link rel="stylesheet" href="https://fonts.googleapis.com/css2?family=Montserrat:wght@400;500;600;700&family=Open+Sans:wght@300;400&display=swap">
<style>
  :root {
    --black: #000000;
    --cyan: #00b0ee;
    --navy: #0d2f6b;
    --name-blue: #2a4f9c;
    --teal: #5bc5cf;
    --grey: #d1d3d4;
    --white: #ffffff;
  }
  * { margin: 0; padding: 0; box-sizing: border-box; }
  html, body { width: 900px; height: 1200px; overflow: hidden; }
  body {
    position: relative;
    background: linear-gradient(180deg, var(--black) 0%, var(--black) 26%, #003548 52%, #0082b4 78%, var(--cyan) 92%, var(--cyan) 100%);
    font-family: "Montserrat", sans-serif;
  }

  /* Brand lockup */
  .brand {
    position: absolute; left: 0; top: 200px; width: 900px;
    text-align: center; color: var(--white);
  }
  .brand__name {
    font-weight: 700; font-size: 50px; letter-spacing: 1px; line-height: 1;
  }
  .brand__tagline {
    margin-top: 20px; font-weight: 700; font-size: 11px; letter-spacing: 9.5px;
    padding-left: 9.5px;
  }

  /* Cards */
  .card {
    position: absolute; left: 160px; width: 580px; height: 355px; overflow: hidden;
  }
  .card--front { top: 341px; background: var(--white); }
  .card--back {
    top: 766px;
    background: radial-gradient(circle at 30% 42%, #16264a 0%, #0a1326 28%, var(--black) 62%);
  }

  .front__visual {
    position: absolute; left: 0; top: 0; width: 258px; height: 342px;
    background: linear-gradient(160deg, rgba(255,255,255,0) 5%, #c4ebf9 40%, #76d0f5 75%, #35bff0 100%);
    opacity: 0.85;
  }
  .front__band {
    position: absolute; left: 0; bottom: 0; width: 100%; height: 13px; background: var(--cyan);
  }
  .person {
    position: absolute; right: 30px; top: 130px; white-space: nowrap; text-align: right;
    font-weight: 700; color: var(--name-blue); font-size: 22px; line-height: 1.2;
  }
  .person__title { font-weight: 500; color: var(--teal); font-size: 16px; }

  .contact {
    position: absolute; right: 0; top: 192px; width: 420px; list-style: none;
  }
  .contact__item {
    display: flex; justify-content: flex-end; align-items: center;
    height: 24px; margin-bottom: 12px;
  }
  .contact__text {
    font-weight: 500; font-size: 11px; color: var(--navy); margin-right: 9px; letter-spacing: 0.2px;
  }
  .contact__tab {
    width: 50px; height: 24px; display: flex; align-items: center; padding-left: 7px;
  }
  .contact__tab--address { background: var(--navy); }
  .contact__tab--phone { background: var(--cyan); }
  .contact__tab--mail { background: var(--teal); }
  .contact__tab--web { background: var(--grey); }
  .contact__tab svg { width: 13px; height: 13px; display: block; }

  .back__visual {
    position: absolute; left: 258px; top: 0; width: 322px; height: 355px;
    background: radial-gradient(ellipse at 60% 30%, rgba(13,47,107,0.75) 0%, rgba(10,36,82,0.45) 45%, rgba(0,0,0,0) 80%);
  }
  .back__brand {
    position: absolute; left: 0; top: 130px; width: 580px; text-align: center; color: var(--white);
  }
  .back__name { font-weight: 700; font-size: 40px; line-height: 1; letter-spacing: 1px; }
  .back__tagline {
    margin-top: 14px; font-weight: 700; font-size: 9px; letter-spacing: 7.5px; padding-left: 7.5px;
  }
  .services {
    position: absolute; left: 0; top: 296px; width: 580px;
    display: flex; align-items: center;
    font-family: "Open Sans", sans-serif; font-weight: 300; font-size: 11.5px; color: var(--white);
  }
  .services__rule { height: 2px; background: var(--teal); flex: 0 0 95px; }
  .services__rule--end { flex: 1 1 auto; }
  .services__list { display: flex; align-items: center; list-style: none; padding: 0 7px 0 6px; white-space: nowrap; }
  .services__item + .services__item::before {
    content: ""; display: inline-block; width: 4px; height: 4px; background: var(--cyan);
    margin: 0 8px 2px 8px; vertical-align: middle;
  }
</style>
</head>
<body>

  <header class="brand">
    <div class="brand__name">BRIGHTWAY</div>
    <div class="brand__tagline">BERATUNG &amp; TRAINING</div>
  </header>

  <section class="card card--front">
    <div class="front__visual" role="img" aria-label="Große, blassblaue Markengrafik als Hintergrunddekoration"></div>
    <p class="person"><span class="person__title">Mag.</span> Lukas Brandauer, <span class="person__title">MSc</span></p>
    <ul class="contact">
      <li class="contact__item">
        <span class="contact__text">Praxis Top 3, Kellergasse 48/2, 1020 Wien</span>
        <span class="contact__tab contact__tab--address">
          <svg viewBox="0 0 14 14"><circle cx="7" cy="7" r="7" fill="#fff"/><path d="M3.8 7.2 7 4.4l3.2 2.8v2.6H3.8z" fill="#0d2f6b"/></svg>
        </span>
      </li>
      <li class="contact__item">
        <span class="contact__text">+43 660 8273916</span>
        <span class="contact__tab contact__tab--phone">
          <svg viewBox="0 0 14 14"><circle cx="7" cy="7" r="7" fill="#fff"/><path d="M5 3.6c.4 0 .8.9.9 1.3.1.4-.5.7-.5 1 .2.8.9 1.5 1.7 1.8.3 0 .6-.6 1-.5.4.1 1.3.5 1.3.9 0 .8-.8 1.3-1.5 1.2C6 9.1 4.7 7.8 4.2 5.9 4 5 4.4 3.6 5 3.6z" fill="#00b0ee"/></svg>
        </span>
      </li>
      <li class="contact__item">
        <span class="contact__text">info@brightway-coaching.eu</span>
        <span class="contact__tab contact__tab--mail">
          <svg viewBox="0 0 14 14"><circle cx="7" cy="7" r="7" fill="#fff"/><rect x="3.5" y="4.8" width="7" height="4.6" fill="none" stroke="#5bc5cf" stroke-width="0.9"/><path d="M3.5 4.8 7 7.5l3.5-2.7" fill="none" stroke="#5bc5cf" stroke-width="0.9"/></svg>
        </span>
      </li>
      <li class="contact__item">
        <span class="contact__text">www.brightway-coaching.eu</span>
        <span class="contact__tab contact__tab--web">
          <svg viewBox="0 0 14 14"><circle cx="7" cy="7" r="7" fill="#fff"/><circle cx="7" cy="7" r="3.6" fill="none" stroke="#d1d3d4" stroke-width="0.8"/><path d="M3.4 7h7.2M7 3.4v7.2" stroke="#d1d3d4" stroke-width="0.8"/></svg>
        </span>
      </li>
    </ul>
    <div class="front__band"></div>
  </section>

  <section class="card card--back">
    <div class="back__visual" role="img" aria-label="Große, dunkelblaue Markengrafik als Hintergrunddekoration"></div>
    <div class="back__brand">
      <div class="back__name">BRIGHTWAY</div>
      <div class="back__tagline">BERATUNG &amp; TRAINING</div>
    </div>
    <div class="services">
      <span class="services__rule"></span>
      <ul class="services__list">
        <li class="services__item">Supervision</li>
        <li class="services__item">Coaching</li>
        <li class="services__item">Aufmerksamkeitstraining</li>
        <li class="services__item">Stressmanagement</li>
      </ul>
      <span class="services__rule services__rule--end"></span>
    </div>
  </section>

</body>
</html>
```